Business Card design for shipping company 'FERNHOLT INTERNATIONAL LTD'

Classic / traditional business card in black Garamond / Times New Roman or similar text for a shipping / marine transport company, containing the following information:

QUOTE

FERNHOLT INTERNATIONAL LTD

MARTIN QUESTEDGE FICS

T: +44 7902 615370
E: cargo@fernholt-example.com

UNQUOTE

Target Market(s)

Marine / Shipping industry

Contact Information for Business Card

FERNHOLT INTERNATIONAL LTD MARTIN QUESTEDGE FICS T: +44 7902 615370 E: cargo@fernholt-example.com

Font styles to use
Serif

Colors

Designer to choose colors to be used in the design.

Requirements
Must have
• Garamond / Times New Roman or similar text in black colour

```html
<!DOCTYPE html>
<html lang="en">
<head>
<meta charset="utf-8">
<title>Fernholt International Ltd – Business Card</title>
<link rel="stylesheet" href="https://fonts.googleapis.com/css2?family=EB+Garamond:wght@400;700&display=swap">
<style>
  :root {
    --page-bg: #e6e4e6;
    --card-bg: #ffffff;
    --ink: #111111;
  }
  * { margin: 0; padding: 0; box-sizing: border-box; }
  html, body {
    width: 1200px;
    height: 1108px;
    overflow: hidden;
    background: var(--page-bg);
  }
  .business-card {
    position: absolute;
    left: 50px;
    top: 239px;
    width: 1100px;
    height: 630px;
    background: var(--card-bg);
    color: var(--ink);
    font-family: "EB Garamond", "Times New Roman", serif;
  }
  .card-line {
    position: absolute;
    left: 0;
    width: 100%;
    text-align: center;
    line-height: 1;
    white-space: nowrap;
  }
  .quote-open    { top: 90px;  font-size: 44px; font-weight: 700; letter-spacing: 1px; }
  .company-name  { top: 208px; font-size: 47px; font-weight: 700; letter-spacing: 0.5px; }
  .person-name   { top: 310px; font-size: 47px; font-weight: 700; letter-spacing: 0.5px; }
  .contact-divider {
    position: absolute;
    left: 252px;
    top: 398px;
    width: 596px;
    height: 36px;
  }
  .contact-phone { top: 468px; font-size: 29px; }
  .contact-email { top: 518px; font-size: 29px; }
  .quote-close {
    position: absolute;
    right: 41px;
    top: 560px;
    font-size: 39px;
    line-height: 1;
    letter-spacing: 0.5px;
  }
</style>
</head>
<body>
  <div class="business-card">
    <p class="card-line quote-open">QUOTE</p>
    <p class="card-line company-name">FERNHOLT INTERNATIONAL LTD</p>
    <p class="card-line person-name">MARTIN QUESTEDGE FICS</p>

    <svg class="contact-divider" viewBox="0 0 596 36" aria-hidden="true">
      <line x1="0" y1="18" x2="252" y2="18" stroke="#111" stroke-width="2"/>
      <line x1="344" y1="18" x2="596" y2="18" stroke="#111" stroke-width="2"/>
      <!-- phone icon -->
      <circle cx="273" cy="18" r="17" fill="#111"/>
      <path d="M265 10 c-2 2 -2 6 1 10 c3 4 7 7 11 7 c2 0 3 -1 4 -3 l-4 -3 l-2 2 c-2 -1 -5 -4 -6 -6 l2 -2 l-3 -4 z" fill="#fff"/>
      <!-- envelope icon -->
      <circle cx="323" cy="18" r="17" fill="#111"/>
      <rect x="312" y="11" width="22" height="15" fill="#fff"/>
      <path d="M312 11 l11 9 l11 -9" fill="none" stroke="#111" stroke-width="2"/>
    </svg>

    <p class="card-line contact-phone">+44 7902 615370</p>
    <p class="card-line contact-email">cargo@fernholt-example.com</p>
    <p class="quote-close">UNQUOTE</p>
  </div>
</body>
</html>
```